Reel Deck Promotional Banner

We are looking for a design for a 33.5" x 79" retractable pop-up banners to used at our live shows. We are a cover band that performs at clubs, corporate events, private parties, and weddings. We would have 2 banners, one on each side of the drum riser, and placed between the lighting trusses. Our website and Facebook page will provide information on what we are about - high energy fun entertainment of live music. We would like some marketing on the banner with logos, etc - something classy that can be used at almost any event. Contact information on the banners would be great. The banners do not have to be the exact same.

Website: www. reeldeckgroup.example
FB: https://www.facebook.example/Reeldeckgroupplano

I have uploaded a logo that can be used. Any other information, images, etc are available not the sites too.

Target Market(s)

New clients looking for a live band

Industry/Entity Type

Live Entertainment

Colors
0054AA
0677BA
7BADD7
CADEEF
E8F1F8
0094D4
00A9DD
6FCCEA
C7EBF8
E9F6FB

Requirements
Must have
• Logo, website address
Nice to have
• Images and excitement

```html
<!DOCTYPE html>
<html lang="en">
<head>
<meta charset="utf-8">
<title>Reel Deck Banners</title>
<link rel="stylesheet" href="https://fonts.googleapis.com/css2?family=Libre+Baskerville:wght@700&display=swap">
<style>
  :root {
    --stage-light: #e2e2e2;
    --stage-mid: #b5b5b5;
    --stage-dark: #4a4a4a;
    --banner-black: #000000;
    --sheen: #262626;
    --white: #ffffff;
    --navy: #1c1f4e;
    --blue-deep: #0054aa;
    --blue-mid: #0677ba;
    --blue-bright: #0094d4;
    --blue-sky: #00a9dd;
    --blue-soft: #6fccea;
    --blue-pale: #c7ebf8;
  }
  * { margin: 0; padding: 0; box-sizing: border-box; }
  html, body { width: 1200px; height: 977px; overflow: hidden; }
  body {
    background: linear-gradient(120deg, var(--stage-light) 0%, var(--stage-mid) 45%, var(--stage-dark) 100%);
    font-family: "Libre Baskerville", Georgia, serif;
    position: relative;
  }
  .banner {
    position: absolute;
    top: 97px;
    width: 481px;
    height: 827px;
    background:
      linear-gradient(135deg, transparent 42%, var(--sheen) 56%, transparent 70%),
      var(--banner-black);
    overflow: hidden;
  }
  .banner--left { left: 108px; }
  .banner--right { left: 618px; }
  .website {
    position: absolute;
    top: 50px;
    width: 100%;
    text-align: center;
    color: var(--white);
    font-size: 19px;
    font-weight: 700;
    letter-spacing: 3px;
  }
  .burst {
    position: absolute;
    top: 116px;
    left: 0;
    width: 481px;
    height: 548px;
    background:
      radial-gradient(ellipse 46% 48% at 50% 50%,
        var(--blue-bright) 0%,
        var(--blue-sky) 28%,
        var(--blue-soft) 44%,
        rgba(111, 204, 234, 0.55) 58%,
        rgba(0, 148, 212, 0.25) 74%,
        transparent 100%);
  }
  .band-name {
    position: absolute;
    top: 362px;
    width: 100%;
    text-align: center;
    color: var(--white);
    font-size: 44px;
    font-weight: 700;
    letter-spacing: 6px;
  }
  .footer {
    position: absolute;
    left: 0;
    bottom: 0;
    width: 100%;
    height: 102px;
    background: var(--white);
  }
  .social-dot {
    position: absolute;
    top: 700px;
    width: 50px;
    height: 50px;
    border-radius: 50%;
    border: 2px solid var(--white);
  }
  .social-dot--one { left: 186px; background: var(--blue-deep); }
  .social-dot--two { left: 248px; background: var(--blue-bright); }
  .handle {
    position: absolute;
    top: 764px;
    width: 100%;
    text-align: center;
    color: var(--navy);
    font-size: 24px;
    font-weight: 700;
    letter-spacing: 6px;
  }
</style>
</head>
<body>
  <section class="banner banner--left">
    <p class="website">www.reeldeckgroup.example</p>
    <div class="burst" role="img" aria-label="Blue equalizer burst radiating from the centre behind the band logo"></div>
    <p class="band-name">REEL DECK</p>
    <div class="footer"></div>
    <span class="social-dot social-dot--one"></span>
    <span class="social-dot social-dot--two"></span>
    <p class="handle">/Reeldeckgroupplano</p>
  </section>

  <section class="banner banner--right">
    <p class="website">www.reeldeckgroup.example</p>
    <div class="burst" role="img" aria-label="Blue equalizer burst radiating from the centre behind the band logo"></div>
    <p class="band-name">REEL DECK</p>
    <div class="footer"></div>
    <span class="social-dot social-dot--one"></span>
    <span class="social-dot social-dot--two"></span>
    <p class="handle">/Reeldeckgroupplano</p>
  </section>
</body>
</html>
```